Startup Jewelry Needs a fully coded Ecommerce Website

Description

We want the full coded woocommerce website - website to be operational and fully integrated with Quidora and other gateways .
We sell jewelry items like rings,ear rings,chain, necklaces etc.

Color Preference
Colors to be used are Velvet red, Black / anthracite, exclusive colors, silver-white, bronze-brown and golden.

Functionalities
Regarding Functions, the store will have functions of typical ecommerce jewelry store using the products/categories for the starting page, going into individual product pages by clicking these images and then leading to a detailed page for one product only.

Target Market
Jewelry-lovers, who appreciate extraordinary things, creative economy/fashion-industries, stylists, Style consultants, outfitter, theaters, operas, production sites, Cocktail-, Dinner and Bride-fashion etc

Look and Feel
Each slider illustrates characteristics of the customer's brand and the style your web design should communicate.

Must have
Logo must be designed

Should Not Have:
- - Dull and common design
- - Messy/unstructured navigation

Industry/Entity Type

Jewelry

Coding

Coded - Design and coding required

```html
<!DOCTYPE html>
<html lang="en">
<head>
<meta charset="utf-8">
<title>Lumen Jewels – Home Page</title>
<link href="https://fonts.googleapis.com/css2?family=Roboto:ital,wght@0,400;0,500;0,700;0,900;1,500&family=Titillium+Web:wght@400&display=swap" rel="stylesheet">
<style>
:root{
  --board:#262626;
  --lime:#66d611;
  --teal:#6cc0b0;
  --red:#e03131;
  --red-dark:#b8242a;
  --gold:#e0a030;
  --ink:#333;
  --muted:#888;
  --line:#e2e2e2;
  --nav:#e6e6e6;
  --white:#fff;
}
*{box-sizing:border-box;margin:0;padding:0}
html,body{width:720px;height:1200px;overflow:hidden}
body{background:var(--board);font-family:"Roboto",sans-serif;color:var(--ink);position:relative}
.abs{position:absolute}
.board-title{top:26px;left:0;width:720px;text-align:center;color:var(--white);font:400 19px/1 "Titillium Web",sans-serif;letter-spacing:2px}
.page{left:110px;top:78px;width:524px;height:1100px;background:var(--white);overflow:hidden}
/* deal bar */
.deal{left:0;top:0;width:524px;height:44px;background:var(--lime)}
.deal-text{top:7px;width:100%;text-align:center;color:var(--white);font-size:5px;font-weight:700}
.countdown{top:18px;left:178px;display:flex;gap:2px;align-items:center}
.digit{width:14px;height:20px;background:#2b2b2b;color:var(--white);font:500 12px/20px "Roboto",sans-serif;text-align:center;border-radius:2px}
.colon{color:#2b2b2b;font-size:10px;font-weight:700;width:4px;text-align:center}
/* header */
.logo{left:42px;top:58px;display:flex;align-items:center;gap:5px}
.logo-mark{width:20px;height:20px;border-radius:50%;border:2px solid #8b6a2e}
.logo-name{font-size:7px;font-weight:700;color:#8b6a2e;line-height:8px;text-transform:uppercase}
.search{left:148px;top:56px;width:180px;height:15px;border:1px solid #ccc;font-size:5px;color:#aaa;padding:4px 6px}
.search-btn{position:absolute;right:0;top:0;width:17px;height:13px;border-left:1px solid #ccc}
.hdr-btn{top:56px;height:15px;border:1px solid #ccc;font-size:4px;color:#aaa;display:flex;align-items:center;gap:6px;padding-right:4px}
.hdr-btn i{width:15px;height:13px;background:#777;display:block;position:relative}
.hdr-btn b{position:absolute;top:-6px;left:12px;width:7px;height:7px;background:var(--teal);font-size:4px;color:#fff;text-align:center;line-height:7px}
/* nav */
.nav{left:0;top:92px;width:524px;height:16px;background:var(--nav);display:flex;padding-left:31px}
.nav a{font-size:5.5px;color:#666;text-decoration:none;padding:0 5px;line-height:16px;text-transform:uppercase}
.nav a.active{background:var(--teal);color:var(--white)}
/* hero */
.hero{left:0;top:108px;width:524px;height:232px;background:radial-gradient(ellipse at 62% 58%,#7a85b3 0%,#4d5b91 35%,#2b3563 70%,#1c2446 100%)}
.hero-copy{left:0;top:48px;width:300px;text-align:center;color:var(--white)}
.hero-kicker{font:italic 500 20px/1 "Roboto",sans-serif}
.hero-sub{font-size:6px;font-weight:700;margin-top:10px;letter-spacing:.4px}
.hero-title{font-size:29px;font-weight:900;margin-top:8px;letter-spacing:.5px}
.hero-offer{font-size:10px;font-weight:700;margin-top:6px}
.hero-offer span{color:var(--teal)}
.btn-dark{display:inline-block;background:#2b2b2b;color:var(--white);font-size:7px;font-weight:700;padding:7px 16px;margin-top:14px}
.dots{left:252px;top:219px;display:flex;gap:4px}
.dots i{width:5px;height:5px;border-radius:50%;background:var(--teal)}
.dots i+i{background:#fff}
/* promos */
.promo{top:365px;width:222px;height:147px;overflow:hidden}
.promo-left{left:32px;background:linear-gradient(90deg,#1c1c1c 0%,#5a3a2a 45%,#2a1c18 100%)}
.promo-right{left:265px;background:radial-gradient(circle at 65% 55%,#f0584e,#d8322b 60%,#b0201c)}
.promo h3{color:var(--white);font-weight:900}
.btn-red{display:inline-block;background:var(--red);color:#fff;font-size:5px;font-weight:700;padding:4px 11px}
.btn-gold{display:inline-block;background:var(--gold);color:#fff;font-size:5px;font-weight:700;padding:4px 11px}
/* free delivery */
.delivery{left:32px;top:532px;width:456px;height:22px;background:var(--teal);display:flex;align-items:center;padding-left:12px;color:var(--white);font-weight:700}
.delivery .shop{position:absolute;right:4px;top:3px;width:70px;height:16px;background:#fff;color:var(--teal);font-size:6px;text-align:center;line-height:16px}
/* tabs & products */
.tabs{left:32px;top:568px;display:flex;font-size:7px;color:#666;gap:0}
.tabs span{padding:0 9px}
.tabs span:first-child{padding-left:0}
.tabs span+span{border-left:1px solid #ccc}
.product{top:583px;width:105px}
.product-photo{height:149px}
.badge{position:absolute;right:6px;width:22px;height:22px;border-radius:50%;background:var(--teal);color:#fff;font-size:4.5px;font-weight:700;text-align:center;line-height:22px}
.product-cat{font-size:5px;color:var(--teal);font-weight:700;margin-top:8px}
.product-name{font-size:6.5px;color:var(--muted);line-height:9px;margin-top:4px}
.product-price{font-size:8px;color:#444;margin-top:4px}
.product-price s{font-weight:700;margin-right:2px}
/* categories */
.section-title{left:32px;top:801px;font-size:6.5px;font-weight:700}
.slider-ctrl{left:458px;top:798px;display:flex;gap:1px}
.slider-ctrl i{width:10px;height:10px;background:#2b2b2b}
.slider-ctrl span{background:#2b2b2b;color:#fff;font-size:4px;font-weight:700;padding:0 5px;line-height:10px}
.category{top:817px;width:105px;height:132px}
.category-label{position:absolute;left:0;bottom:11px;width:100%;height:28px;background:rgba(60,60,60,.75);color:#fff;text-align:center;padding-top:6px}
.category-label strong{display:block;font-size:8.5px}
.category-label small{font-size:4.5px}
/* features */
.feature{top:971px;width:143px;height:45px;border:1px solid var(--line);padding:7px 8px 0 32px}
.feature svg{position:absolute;left:10px;top:9px}
.feature h4{font-size:8px;font-weight:500;color:#444}
.feature p{font-size:5px;color:var(--muted);line-height:7.5px;margin-top:3px}
/* footer */
.footer{left:0;top:1034px;width:524px;height:66px;background:var(--red)}
.cards{left:32px;top:20px;display:flex;gap:3px}
.cards span{width:24px;height:14px;background:#fff;border-radius:1px;font-size:4.5px;font-weight:700;color:#555;text-align:center;line-height:14px}
.social{left:374px;top:20px;display:flex;gap:5px}
.social i{width:14px;height:14px;background:rgba(255,255,255,.85);display:block}
.footer-line{left:32px;top:48px;width:456px;height:1px;background:rgba(255,255,255,.3)}
.copyright{top:56px;width:100%;text-align:center;font-size:4.5px;color:#fff}
</style>
</head>
<body>
<div class="abs board-title">DESIGN IDEA - 02 ( Home Page)</div>

<main class="abs page">
  <section class="abs deal">
    <p class="abs deal-text">Limited Time Deal : 15% Off on Any Purchase [ Use COUPON Code : EC10PDT ]</p>
    <div class="abs countdown">
      <span class="digit">0</span><span class="digit">1</span><span class="colon">:</span>
      <span class="digit">0</span><span class="digit">4</span><span class="colon">:</span>
      <span class="digit">2</span><span class="digit">0</span><span class="colon">:</span>
      <span class="digit">4</span><span class="digit">5</span>
    </div>
  </section>

  <header>
    <div class="abs logo"><span class="logo-mark"></span><span class="logo-name">Lumen<br>Jewels</span></div>
    <div class="abs search">Search Products...
      <span class="search-btn"><svg width="17" height="13" viewBox="0 0 17 13"><circle cx="8" cy="6" r="2.5" fill="none" stroke="#555" stroke-width="1"/><line x1="10" y1="8" x2="12" y2="10" stroke="#555"/></svg></span>
    </div>
    <div class="abs hdr-btn" style="left:375px;width:56px"><i><b>0</b></i>WISH LIST</div>
    <div class="abs hdr-btn" style="left:440px;width:47px"><i><b>1</b></i>CART ⌄</div>
  </header>

  <nav class="abs nav">
    <a class="active">Home</a><a>Shop</a><a>Rings</a><a>Ear Rings</a><a>Necklace</a><a>Chain</a><a>My Account</a><a>Checkout</a><a>Cart</a>
  </nav>

  <section class="abs hero" role="img" aria-label="Close-up photo of diamond rings displayed on blue velvet stands">
    <div class="abs hero-copy">
      <div class="hero-kicker" style="padding-left:30px">Style Up!</div>
      <div class="hero-sub">WITH OUR AMAZING COLLECTION OF</div>
      <div class="hero-title">DIAMOND RINGS</div>
      <div class="hero-offer">ORDER NOW. <span>GET 10% OFF</span></div>
      <span class="btn-dark">START SHOPPING</span>
    </div>
    <div class="abs dots"><i></i><i></i></div>
  </section>

  <section class="abs promo promo-left" role="img" aria-label="Photo of a smiling woman wearing diamond earrings and necklace">
    <div class="abs" style="right:14px;top:50px;color:#fff;font-size:9px;font-weight:700">DIAMOND</div>
    <h3 class="abs" style="left:14px;top:63px;font-size:32px;letter-spacing:.5px">COLLECTION</h3>
    <div class="abs" style="right:14px;top:98px;color:#fff;font-size:9px;font-weight:700">GET 25% DISCOUNT</div>
    <span class="abs btn-red" style="right:14px;top:116px">START SHOPPING</span>
  </section>

  <section class="abs promo promo-right" role="img" aria-label="Photo of two gold wedding rings on red lace">
    <div class="abs" style="left:13px;top:15px;color:#fff;font-size:9px;font-weight:700">20% DISCOUNT</div>
    <h3 class="abs" style="left:13px;top:28px;font-size:32px;line-height:36px;letter-spacing:1px">WEDDING<br>RINGS</h3>
    <span class="abs btn-gold" style="left:13px;top:105px">START SHOPPING</span>
  </section>

  <section class="abs delivery">
    <span style="font-size:9.5px">FREE DELIVERY!</span>
    <span style="font-size:7.5px;margin-left:8px">WE PROVIDE FREE SHIPPING ON ALL ORDERS MORE THAN $100</span>
    <span class="shop">SHOP NOW</span>
  </section>

  <div class="abs tabs"><span>BEST SELLERS</span><span>NEW ARRIVALS</span><span>TOP RATED</span></div>

  <article class="abs product" style="left:32px">
    <div class="product-photo" role="img" aria-label="Gold necklace set with earrings" style="background:radial-gradient(circle,#e8c060,#c99a3a 55%,#eef0ee 90%)"></div>
    <span class="badge" style="top:6px">SALE!</span><span class="badge" style="top:33px">NEW!</span>
    <div class="product-cat">NECKLACE</div>
    <div class="product-name">Gold Plated Designer Engraved Necklace Set With Earrings</div>
    <div class="product-price"><s>$159.00</s> $119.00</div>
  </article>
  <article class="abs product" style="left:148px">
    <div class="product-photo" role="img" aria-label="White gold heart diamond pendant" style="background:radial-gradient(circle at 50% 65%,#c8e4ee,#f4f6f7 60%,#fff)"></div>
    <span class="badge" style="top:6px">SALE!</span><span class="badge" style="top:33px">NEW!</span>
    <div class="product-cat">NECKLACE</div>
    <div class="product-name">14 Karat White Gold Heart Diamond Pendant</div>
    <div class="product-price"><s>$159.99</s> $139.99</div>
  </article>
  <article class="abs product" style="left:265px">
    <div class="product-photo" role="img" aria-label="Long diamond necklace on a black display bust" style="background:radial-gradient(circle at 50% 45%,#555,#1a1a1a 65%,#000)"></div>
    <span class="badge" style="top:6px">SALE!</span><span class="badge" style="top:33px">NEW!</span>
    <div class="product-cat">NECKLACE</div>
    <div class="product-name">Long Diamond Necklace With Earrings</div>
    <div class="product-price"><s>$219.99</s> $189.99</div>
  </article>
  <article class="abs product" style="left:382px">
    <div class="product-photo" role="img" aria-label="Silver ring with cubic zircons on black" style="background:radial-gradient(circle at 45% 50%,#bbb,#333 55%,#000)"></div>
    <span class="badge" style="top:6px">SALE!</span><span class="badge" style="top:33px">NEW!</span>
    <div class="product-cat">RINGS</div>
    <div class="product-name">Designer Silver Nail Ring With Cubic Zircons</div>
    <div class="product-price"><s>$109.99</s> $89.99</div>
  </article>

  <h2 class="abs section-title">BROWSE OUR CATEGORIES</h2>
  <div class="abs slider-ctrl"><i></i><i></i><span>VIEW ALL</span></div>

  <a class="abs category" style="left:32px;background:linear-gradient(135deg,#e9e4e2,#c9b8b0 60%,#8a7a72)" role="img" aria-label="Photo of a woman holding a chain pendant">
    <span class="category-label"><strong>CHAIN</strong><small>1 PRODUCTS</small></span></a>
  <a class="abs category" style="left:148px;background:linear-gradient(135deg,#6a0f1e,#a0283a 50%,#d9a88a)" role="img" aria-label="Photo of a woman wearing earrings on dark red background">
    <span class="category-label"><strong>EAR RINGS</strong><small>4 PRODUCTS</small></span></a>
  <a class="abs category" style="left:265px;background:radial-gradient(circle at 50% 50%,#8a8a8a,#2a2a2a 60%,#111)" role="img" aria-label="Photo of a diamond necklace on a dark display">
    <span class="category-label"><strong>NECKLACE</strong><small>3 PRODUCTS</small></span></a>
  <a class="abs category" style="left:382px;background:radial-gradient(circle at 55% 45%,#f2f2f2,#b5b5b5 55%,#7a7a7a)" role="img" aria-label="Black and white photo of a diamond ring">
    <span class="category-label"><strong>RINGS</strong><small>2 PRODUCTS</small></span></a>

  <div class="abs feature" style="left:32px">
    <svg width="14" height="18" viewBox="0 0 14 18"><path d="M3 8V5a4 4 0 0 1 8 0v3" fill="none" stroke="#333" stroke-width="2"/><rect x="1" y="8" width="12" height="9" fill="#333"/></svg>
    <h4>Secure Payments</h4><p>Lorem ipsum dolor sit amet. Morbi at nisl lorem, vel porttitor justo.</p>
  </div>
  <div class="abs feature" style="left:187px">
    <svg width="14" height="20" viewBox="0 0 14 20"><text x="1" y="17" font-family="Roboto,sans-serif" font-size="20" font-weight="700" fill="#333">$</text></svg>
    <h4>Money Back Guarantee</h4><p>Lorem ipsum dolor sit amet. Morbi at nisl lorem, vel porttitor justo.</p>
  </div>
  <div class="abs feature" style="left:343px">
    <svg width="18" height="14" viewBox="0 0 18 14"><rect x="0" y="2" width="11" height="8" fill="#333"/><path d="M11 5h4l3 3v2h-7z" fill="#333"/><circle cx="4" cy="11" r="2" fill="#333"/><circle cx="14" cy="11" r="2" fill="#333"/></svg>
    <h4>Free Delivery</h4><p>Pellentesque habitant morbi netus tristique senectus et malesuada.</p>
  </div>

  <footer class="abs footer">
    <div class="abs cards"><span>Quidora</span><span>Verapay</span><span>Coinly</span><span>Tallo</span></div>
    <div class="abs social"><i></i><i></i><i></i><i></i><i></i><i></i></div>
    <div class="abs footer-line"></div>
    <p class="abs copyright">Lumen Jewels Copyright © 2016.</p>
  </footer>
</main>
</body>
</html>
```